Marlo Tidy Yard Website

We need a website design for this new company. I've attached the company logo. This company is in the construction industry that provides general labor, maintenance and cleaning for construction sites. We want a clean and simple website that can be easy to navigate.

Target Market(s)

Construction industry

Industry/Entity Type

Construction

Number of Pages Required

2 page

Font styles to use
Sans Serif

```html
<!DOCTYPE html>
<html lang="en">
<head>
<meta charset="utf-8">
<title>Marlo Tidy Yard</title>
<link href="https://fonts.googleapis.com/css2?family=Montserrat:ital,wght@0,400;0,500;0,600;0,700;1,400&display=swap" rel="stylesheet">
<style>
:root{
  --navy:#121a6f;
  --orange:#f36c10;
  --ink:#1c1c1c;
  --muted:#8a8a8a;
  --line:#e3e3e3;
  --grey-bg:#f4f4f4;
  --footer-bg:#2a2a2a;
  --white:#ffffff;
}
*{box-sizing:border-box;margin:0;padding:0}
html,body{width:730px;height:1200px;overflow:hidden;background:var(--white)}
body{position:relative;font-family:"Montserrat",sans-serif;color:var(--ink)}
.abs{position:absolute}

/* header */
.brand{left:142px;top:0;width:77px;height:46px;background:var(--white);display:flex;flex-direction:column;justify-content:center;align-items:center;z-index:3;box-shadow:0 2px 4px rgba(0,0,0,.12)}
.brand span{font-weight:700;color:var(--navy);font-size:10px;line-height:11px;letter-spacing:.2px;text-align:center}
.contact-top{top:7px;display:flex;align-items:center;gap:5px;font-size:5.8px;color:var(--ink);z-index:3}
.contact-top .ic{width:13px;height:13px;border:1px solid var(--orange);border-radius:50%;display:flex;align-items:center;justify-content:center}
.mainnav{left:219px;top:26px;width:368px;height:20px;background:var(--navy);display:flex;align-items:center;justify-content:space-around;padding:0 8px;z-index:3}
.mainnav a{color:var(--white);font-size:5.4px;font-weight:500;text-decoration:none;letter-spacing:.2px}
.mainnav a.active{color:var(--orange)}
.mainnav i{width:1px;height:5px;background:rgba(255,255,255,.6)}

/* hero */
.hero{left:0;top:46px;width:730px;height:260px;background:linear-gradient(100deg,#e7a24e 0%,#c58042 14%,#3a3a40 34%,#1d2029 55%,#4d6a8b 78%,#1a1e26 100%)}
.hero-title{left:424px;top:138px;width:146px;height:19px;background:var(--navy);color:var(--white);font-weight:600;font-size:10.5px;letter-spacing:1.6px;display:flex;align-items:center;justify-content:center;clip-path:polygon(4% 0,100% 0,96% 100%,0 100%)}
.hero-btn{left:486px;top:164px;width:74px;height:19px;background:var(--orange);color:var(--white);font-weight:600;font-size:7px;letter-spacing:.6px;display:flex;align-items:center;justify-content:center;clip-path:polygon(6% 0,100% 0,94% 100%,0 100%)}
.slashes{top:0}
.wave{left:0;top:260px}
.dots{left:368px;top:265px;width:33px;height:10px;background:var(--white);border-radius:2px;display:flex;align-items:center;justify-content:center;gap:2px;box-shadow:0 1px 3px rgba(0,0,0,.2)}
.dots b{width:3px;height:3px;border-radius:50%;background:#b9c2d3}
.dots b.on{background:var(--orange)}

/* about */
.about-photo{left:142px;top:322px;width:210px;height:84px;background:linear-gradient(135deg,#c9d3e2,#8b7c6a 55%,#5a5048);}
.about-shadow{left:150px;top:410px;width:195px;height:10px;border-radius:50%;background:radial-gradient(closest-side,rgba(0,0,0,.2),transparent)}
.about-h{left:371px;top:320px;font-size:12.5px;font-weight:600;color:var(--ink)}
.about-p{left:371px;width:218px;font-size:5.1px;line-height:10.4px;color:var(--muted)}
.why-h{left:142px;top:445px;font-size:6.6px;font-weight:700;color:var(--navy);letter-spacing:.2px}
.why-h em,.section-h em{font-style:normal;color:var(--orange)}
.why{top:464px;width:150px;display:flex;gap:11px}
.why .circ{flex:none;width:32px;height:32px;border-radius:50%;background:var(--orange);display:flex;align-items:center;justify-content:center}
.why h4{font-size:6.6px;font-weight:600;margin:2px 0 3px}
.why p{font-size:5px;line-height:9px;color:var(--muted)}

/* services */
.services{left:0;top:532px;width:730px;height:216px;background:var(--grey-bg)}
.section-h{font-size:9px;font-weight:700;color:var(--navy);width:730px;text-align:center;letter-spacing:.3px}
.rule{left:354px;width:21px;height:1.5px;background:#9a9a9a}
.card{top:602px;width:103px;height:114px;background:var(--white);box-shadow:0 1px 4px rgba(0,0,0,.12);text-align:center;padding-top:10px}
.card h5{font-size:6.3px;font-weight:700;line-height:10.5px;margin-top:4px;color:var(--ink)}
.card p{font-size:5px;line-height:9px;color:#555;margin-top:3px}
.card a{display:block;font-size:4.8px;font-weight:700;color:var(--orange);text-decoration:none;margin-top:4px}

/* testimonials */
.t-card{left:192px;top:822px;width:346px;height:111px;background:var(--white);box-shadow:0 1px 5px rgba(0,0,0,.12)}
.avatar{left:355px;top:813px;width:21px;height:21px;border-radius:50%;background:linear-gradient(#d8d8d8,#9d9d9d);border:1.5px solid var(--white);box-shadow:0 0 2px rgba(0,0,0,.3)}
.t-name{left:192px;width:346px;top:838px;text-align:center;font-size:5.6px;font-weight:700;color:var(--orange)}
.t-role{left:192px;width:346px;top:845px;text-align:center;font-size:4.8px;font-style:italic;color:#555}
.t-quote{left:210px;width:310px;top:859px;text-align:center;font-size:5.2px;line-height:10.6px;font-style:italic;color:#555}
.qmark{font-size:16px;font-weight:700;color:#d3d3d3;line-height:1}
.arrow{width:15px;height:15px;border-radius:50%;border:1px solid var(--line);background:var(--white);display:flex;align-items:center;justify-content:center}

/* contact */
.contact-band{left:0;top:960px;width:730px;height:1px;background:var(--line)}
.info-col{left:142px;top:960px;width:179px;height:198px;border-left:1px solid var(--line);border-right:1px solid var(--line)}
.foot-brand{left:154px;top:988px;width:56px;font-size:8px;line-height:9.5px;font-weight:700;color:var(--navy)}
.foot-about{left:220px;top:982px;width:93px;font-size:4.7px;line-height:8.5px;color:#555}
.hline{left:142px;width:179px;height:1px;background:var(--line)}
.lbl{font-size:5px;font-weight:500;color:var(--ink)}
.val{font-size:4.8px;color:#444}
.soc{top:1086px;width:15px;height:15px;border-radius:50%;border:1px solid #444;display:flex;align-items:center;justify-content:center}
.field{border:1px solid var(--line);background:var(--white)}
.send{left:333px;top:1119px;width:64px;height:16px;background:var(--orange);color:var(--white);font-size:5px;font-weight:600;display:flex;align-items:center;justify-content:center}

/* footer */
.footer{left:0;top:1158px;width:730px;height:42px;background:var(--footer-bg)}
.copy{left:142px;top:1177px;font-size:5px;color:#cfcfcf}
.footnav{top:1177px;font-size:5px;color:var(--white);font-weight:500}
</style>
</head>
<body>

<!-- header -->
<div class="abs brand"><span>MARLO<br>TIDY YARD</span></div>
<div class="abs contact-top" style="left:412px">
  <span class="ic"><svg width="7" height="5" viewBox="0 0 7 5"><rect x=".4" y=".4" width="6.2" height="4.2" fill="none" stroke="#f36c10" stroke-width=".8"/><path d="M.4.4 3.5 3 6.6.4" fill="none" stroke="#f36c10" stroke-width=".8"/></svg></span>
  info@marlotidyyard.com
</div>
<div class="abs contact-top" style="left:512px">
  <span class="ic"><svg width="7" height="7" viewBox="0 0 24 24"><path fill="#f36c10" d="M6.6 10.8a15 15 0 0 0 6.6 6.6l2.2-2.2c.3-.3.7-.4 1-.2 1.1.4 2.3.6 3.6.6.6 0 1 .4 1 1V20c0 .6-.4 1-1 1A17 17 0 0 1 3 4c0-.6.4-1 1-1h3.5c.6 0 1 .4 1 1 0 1.3.2 2.5.6 3.6.1.3 0 .7-.2 1z"/></svg></span>
  +617 555 010 2040
</div>
<nav class="abs mainnav">
  <a class="active">HOME</a><i></i><a>ABOUT US</a><i></i><a>SERVICES</a><i></i><a>PROJECTS</a><i></i><a>GALLERY</a><i></i><a>CONTACT US</a>
</nav>

<!-- hero -->
<div class="abs hero" role="img" aria-label="Construction worker in hard hat and safety vest holding a chainsaw in front of a building site with scaffolding at sunset"></div>
<div class="abs hero-title">MARLO TIDY YARD</div>
<svg class="abs" style="left:570px;top:138px" width="18" height="19" viewBox="0 0 18 19"><path d="M4 0h3L2 19H-1zM10 0h3L8 19H5z" fill="#f36c10"/></svg>
<div class="abs hero-btn">LEARN MORE</div>
<svg class="abs" style="left:556px;top:164px" width="18" height="19" viewBox="0 0 18 19"><path d="M6 0h3L4 19H1zM12 0h3L10 19H7z" fill="#f36c10"/></svg>
<svg class="abs wave" width="730" height="50" viewBox="0 0 730 50">
  <path d="M0 46 C120 44 230 12 368 12 C500 12 620 30 730 38 L730 50 L0 50Z" fill="#ffffff"/>
  <path d="M170 38 C250 22 300 12 368 12 C500 12 620 30 730 38" fill="none" stroke="#f36c10" stroke-width="2"/>
</svg>
<div class="abs dots"><b class="on"></b><b></b><b></b><b></b><b></b></div>

<!-- about -->
<div class="abs about-photo" role="img" aria-label="Workers building a concrete structure, shown through large block lettering"></div>
<div class="abs about-shadow"></div>
<h2 class="abs about-h">About Us</h2>
<p class="abs about-p" style="top:337px">Lorem ipsum dolor sit amet, consectetur adipiscing elit. Sed nec orci convallis purus consequat placerat ut at velit.</p>
<p class="abs about-p" style="top:369px">Donec lacinia ultricies enim, id rhoncus urna efficitur sed. Proin ultricies sem quis orci rhoncus condimentum. Nunc nec sem ut nisi pellentesque scelerisque sit amet quis ante. Mauris congue, velit eget porta congue, felis risus dapibus eros, ac porttitor enim sapien vel tortor.</p>

<h3 class="abs why-h">WHY <em>CHOOSE US</em></h3>
<div class="abs why" style="left:142px">
  <div class="circ"><svg width="12" height="12" viewBox="0 0 24 24" fill="none" stroke="#fff" stroke-width="2"><path d="M9 18h6M10 21h4M12 3a6 6 0 0 0-3.5 10.9V16h7v-2.1A6 6 0 0 0 12 3z"/><path d="M12 0v1M3 9H2M22 9h-1"/></svg></div>
  <div><h4>Experience</h4><p>Lorem ipsum dolor sit amet, consectetur adipiscing elit. Sed nec orci convallis purus.</p></div>
</div>
<div class="abs why" style="left:294px">
  <div class="circ"><svg width="12" height="12" viewBox="0 0 24 24" fill="#fff"><path d="M10 2h4l.6 3 2.3 1 2.6-1.7 2.8 2.8-1.7 2.6 1 2.3 3 .6v4l-3 .6-1 2.3 1.7 2.6-2.8 2.8-2.6-1.7-2.3 1-.6 3h-4l-.6-3-2.3-1-2.6 1.7-2.8-2.8 1.7-2.6-1-2.3-3-.6v-4l3-.6 1-2.3L1.7 7.1l2.8-2.8 2.6 1.7 2.3-1zM12 8.5a3.5 3.5 0 1 0 0 7 3.5 3.5 0 0 0 0-7z" transform="scale(.92) translate(1 1)"/></svg></div>
  <div><h4>Experts</h4><p>Lorem ipsum dolor sit amet, consectetur adipiscing elit. Sed nec orci convallis purus.</p></div>
</div>
<div class="abs why" style="left:446px">
  <div class="circ"><svg width="12" height="12" viewBox="0 0 24 24" fill="none" stroke="#fff" stroke-width="2"><circle cx="12" cy="9" r="6"/><circle cx="12" cy="9" r="2.5"/><path d="M8.5 14 7 22l5-3 5 3-1.5-8"/></svg></div>
  <div><h4>Satisfaction</h4><p>Lorem ipsum dolor sit amet, consectetur adipiscing elit. Sed nec orci convallis purus.</p></div>
</div>

<!-- services -->
<div class="abs services"></div>
<h2 class="abs section-h" style="left:0;top:560px">WHAT <em>WE DO</em></h2>
<div class="abs rule" style="top:576px"></div>

<div class="abs card" style="left:192px">
  <svg width="20" height="24" viewBox="0 0 20 24" fill="none" stroke="#f36c10" stroke-width="1.2"><path d="M4 9a6 6 0 0 1 12 0z"/><path d="M2 9h16"/><path d="M5 10a5 5 0 0 0 10 0"/><path d="M2 23v-3a5 5 0 0 1 5-5h6a5 5 0 0 1 5 5v3zM10 15v8"/></svg>
  <h5>GENERAL LABOR FOR<br>CONSTRUCTION</h5>
  <p>Lorem ipsum dolor sit amet,<br>consectetur adipiscing elit.<br>Sed nec orci convallis purus.</p>
  <a>READ MORE</a>
</div>
<div class="abs card" style="left:314px">
  <svg width="24" height="24" viewBox="0 0 24 24" fill="none" stroke="#f36c10" stroke-width="1.2"><circle cx="15" cy="8" r="4"/><circle cx="15" cy="8" r="1.5"/><circle cx="7" cy="15" r="3"/><path d="M15 2v2M15 12v2M9 8h2M19 8h2M4 22l6-6M18 22l-4-4"/></svg>
  <h5>MAINTENANCE FOR<br>CONSTRUCTION</h5>
  <p>Lorem ipsum dolor sit amet,<br>consectetur adipiscing elit.<br>Sed nec orci convallis purus.</p>
  <a>READ MORE</a>
</div>
<div class="abs card" style="left:435px">
  <svg width="24" height="24" viewBox="0 0 24 24" fill="#f36c10"><circle cx="7" cy="4" r="2.5"/><path d="M4 8h6l1 6-2 1 1 8H8l-1-6-1 6H4l1-9zM11 10l8 8-1 1-8-8z"/><path d="M16 22l3-6 4 6z"/></svg>
  <h5>CLEANING FOR<br>CONSTRUCTION</h5>
  <p>Lorem ipsum dolor sit amet,<br>consectetur adipiscing elit.<br>Sed nec orci convallis purus.</p>
  <a>READ MORE</a>
</div>

<!-- testimonials -->
<h2 class="abs section-h" style="left:0;top:773px;color:var(--orange)">TESTIMONIALS</h2>
<div class="abs rule" style="top:790px"></div>
<div class="abs t-card"></div>
<div class="abs avatar" role="img" aria-label="Customer portrait"></div>
<div class="abs t-name">RAVI HOLDEN</div>
<div class="abs t-role">Customer</div>
<div class="abs qmark" style="left:199px;top:830px">&ldquo;</div>
<div class="abs qmark" style="left:520px;top:914px">&rdquo;</div>
<p class="abs t-quote">Lorem ipsum dolor sit amet, consectetur adipiscing elit. Sed nec orci convallis purus consequat placerat ut at velit. Donec lacinia ultricies enim, id rhoncus urna efficitur sed. Proin ultricies sem quis orci rhoncus condimentum. Nunc nec sem ut nisi pellentesque scelerisque sit amet quis ante. Mauris congue, velit eget porta congue, felis risus dapibus eros, ac porttitor enim sapien vel tortor. Vivamus elementum posuere lectus, quis malesuada lacus consequat a. Fusce auctor tellus dapibus neque commodo accumsan.</p>
<div class="abs arrow" style="left:159px;top:871px"><svg width="4" height="6" viewBox="0 0 4 6"><path d="M3 .5.8 3 3 5.5" fill="none" stroke="#999" stroke-width=".8"/></svg></div>
<div class="abs arrow" style="left:554px;top:871px"><svg width="4" height="6" viewBox="0 0 4 6"><path d="M1 .5 3.2 3 1 5.5" fill="none" stroke="#999" stroke-width=".8"/></svg></div>

<!-- contact -->
<div class="abs contact-band"></div>
<div class="abs info-col"></div>
<div class="abs foot-brand">MARLO<br>TIDY YARD</div>
<p class="abs foot-about">Lorem ipsum dolor sit amet, consectetur adipiscing elit. Sed nec orci convallis purus consequat placerat ut at velit. ut nisi pellentesque scelerisque sit amet quis ante.</p>
<div class="abs hline" style="top:1040px"></div>
<div class="abs lbl" style="left:154px;top:1052px">ADDRESS</div>
<div class="abs val" style="left:154px;top:1062px;line-height:9px">40123 Lorem ipsum dolor sit amet,<br>consectetur adipiscing elit.</div>
<div class="abs soc" style="left:155px"><svg width="7" height="7" viewBox="0 0 10 10" fill="none" stroke="#333" stroke-width="1"><rect x="1" y="1" width="8" height="8" rx="2"/><circle cx="5" cy="5" r="2"/></svg></div>
<div class="abs soc" style="left:174px"><svg width="7" height="7" viewBox="0 0 10 10" fill="none" stroke="#333" stroke-width="1"><rect x="1" y="1" width="8" height="8" rx="1"/></svg></div>
<div class="abs soc" style="left:193px"><svg width="7" height="7" viewBox="0 0 10 10" fill="none" stroke="#333" stroke-width="1"><rect x="1" y="2" width="8" height="6" rx="1.5"/></svg></div>
<div class="abs hline" style="top:1112px"></div>
<div class="abs" style="left:231px;top:1112px;width:1px;height:46px;background:var(--line)"></div>
<div class="abs lbl" style="left:154px;top:1127px">TELEPHONE :</div>
<div class="abs val" style="left:154px;top:1138px">+617 555 010 2040</div>
<div class="abs lbl" style="left:242px;top:1127px">E-mail :</div>
<div class="abs val" style="left:242px;top:1138px">info@marlotidyyard.com</div>

<div class="abs lbl" style="left:333px;top:982px">FULL NAME</div>
<div class="abs field" style="left:333px;top:992px;width:124px;height:19px"></div>
<div class="abs lbl" style="left:464px;top:982px">EMAIL</div>
<div class="abs field" style="left:464px;top:992px;width:124px;height:19px"></div>
<div class="abs lbl" style="left:333px;top:1020px">TELEPHONE</div>
<div class="abs field" style="left:333px;top:1030px;width:124px;height:19px"></div>
<div class="abs lbl" style="left:464px;top:1020px">SUBJECT</div>
<div class="abs field" style="left:464px;top:1030px;width:124px;height:19px"></div>
<div class="abs lbl" style="left:333px;top:1057px">MESSAGE</div>
<div class="abs field" style="left:333px;top:1067px;width:255px;height:42px"></div>
<div class="abs send">SEND MESSAGE</div>

<!-- footer -->
<footer class="abs footer"></footer>
<div class="abs copy">Copyright &copy; 2019 Marlo Tidy Yard. All rights reserved.</div>
<div class="abs footnav" style="left:349px">HOME</div>
<div class="abs footnav" style="left:383px">ABOUT US</div>
<div class="abs footnav" style="left:427px">SERVICES</div>
<div class="abs footnav" style="left:470px">PROJECTS</div>
<div class="abs footnav" style="left:515px">GALLERY</div>
<div class="abs footnav" style="left:555px">CONTACT US</div>

</body>
</html>
```